Brand owner needs a packaging design for a Standing Fan

We need a full color packaging design for a standing floor fan. Please see attached files for further information.

Industry/Entity Type

Floor

```html
<!DOCTYPE html>
<html lang="en">
<head>
<meta charset="utf-8">
<title>PolarGust Pedestal Fan Packaging</title>
<link rel="stylesheet" href="https://fonts.googleapis.com/css2?family=Signika:wght@400;600;700&display=swap">
<style>
  :root {
    --stage: #e4e5e7;
    --navy: #2b3a73;
    --navy-deep: #1d2a5c;
    --sky: #6ec3ef;
    --sky-light: #bfe4f6;
    --ice: #eef7fc;
    --white: #ffffff;
    --side-top: #d7e6f0;
    --side-bottom: #9fc9e4;
    --fan-dark: #1c1f27;
  }
  html, body {
    margin: 0;
    width: 1200px;
    height: 1022px;
    overflow: hidden;
    background: var(--stage);
    font-family: "Signika", "Trebuchet MS", sans-serif;
  }
  p, h1, h2 { margin: 0; }

  .package-side {
    position: absolute;
    left: 300px;
    top: 130px;
    width: 58px;
    height: 770px;
    overflow: hidden;
    background: linear-gradient(180deg, var(--side-top) 0%, var(--ice) 40%, var(--side-bottom) 100%);
    box-shadow: inset -6px 0 10px rgba(0,0,0,0.08);
  }
  .side-band {
    position: absolute;
    left: 0; top: 0;
    width: 58px; height: 140px;
    background: var(--navy);
    border-bottom: 16px solid var(--sky);
  }
  .side-brand {
    position: absolute;
    left: 29px;
    top: 330px;
    transform: translate(-50%, -50%) rotate(-90deg);
    display: flex;
    align-items: center;
    gap: 10px;
    white-space: nowrap;
  }
  .side-brand .brand-dot { width: 30px; height: 30px; background: var(--navy); }
  .side-brand .brand-name { font-size: 30px; color: var(--navy); }

  .package-front {
    position: absolute;
    left: 358px;
    top: 130px;
    width: 532px;
    height: 770px;
    overflow: hidden;
    background: linear-gradient(180deg, var(--white) 0%, var(--ice) 45%, var(--sky-light) 100%);
    box-shadow: 0 10px 30px rgba(0,0,0,0.15);
  }
  .swirl-backdrop {
    position: absolute;
    left: -90px;
    top: 300px;
    width: 440px;
    height: 480px;
    border-radius: 50%;
    background: radial-gradient(circle at 50% 50%, rgba(110,195,239,0.55) 0%, rgba(60,110,170,0.35) 45%, rgba(191,228,246,0) 72%);
  }
  .top-band {
    position: absolute;
    left: 0; top: 0;
    width: 532px; height: 160px;
  }
  .brand-lockup {
    position: absolute;
    left: 205px;
    top: 48px;
    display: flex;
    align-items: center;
    gap: 12px;
  }
  .brand-dot {
    display: block;
    width: 50px; height: 50px;
    border-radius: 50%;
    background: var(--sky-light);
  }
  .brand-name {
    color: var(--white);
    font-weight: 600;
    font-size: 48px;
    line-height: 1;
  }
  .headline {
    position: absolute;
    right: 10px;
    top: 158px;
    color: var(--navy);
    font-weight: 600;
    font-size: 24px;
    line-height: 48px;
    white-space: nowrap;
  }
  .headline .size { font-size: 44px; font-weight: 700; }
  .product-type {
    position: absolute;
    right: 10px;
    top: 212px;
    text-align: right;
    line-height: 1;
    font-weight: 600;
  }
  .product-type .word-pedestal { display: block; font-size: 66px; color: var(--sky); }
  .product-type .word-fan { display: block; font-size: 58px; color: var(--navy); }
  .feature-tilt {
    position: absolute;
    right: 10px;
    top: 350px;
    text-align: right;
    color: var(--navy);
    font-weight: 600;
    line-height: 1.15;
  }
  .feature-tilt .lead { display: block; font-size: 22px; }
  .feature-tilt .small { display: block; font-size: 16px; }
  .tilt-icon {
    position: absolute;
    left: 412px;
    top: 440px;
    width: 112px;
    height: 118px;
  }
  .feature-positions {
    position: absolute;
    right: 14px;
    top: 562px;
    text-align: right;
    color: var(--navy);
    font-weight: 600;
    font-size: 24px;
    line-height: 32px;
  }
  .feature-height {
    position: absolute;
    left: 230px;
    top: 502px;
    color: var(--navy);
    font-weight: 600;
    font-size: 23px;
    line-height: 30px;
  }
  .product-photo {
    position: absolute;
    left: 132px;
    top: 228px;
    width: 90px;
    height: 516px;
    background: linear-gradient(180deg, #2b2f3a 0%, var(--fan-dark) 60%, #2a2c33 100%);
    border-radius: 45px 45px 22px 22px;
    opacity: 0.9;
  }
  .model-name {
    position: absolute;
    right: 12px;
    top: 664px;
    font-size: 50px;
    line-height: 1.1;
    font-weight: 600;
    color: var(--navy-deep);
  }
</style>
</head>
<body>
  <aside class="package-side">
    <div class="side-band"></div>
    <div class="side-brand">
      <span class="brand-dot"></span>
      <span class="brand-name">PolarGust</span>
    </div>
  </aside>

  <main class="package-front">
    <div class="swirl-backdrop" role="img" aria-label="Soft blue swirl of moving air behind the fan"></div>

    <svg class="top-band" viewBox="0 0 532 160" aria-hidden="true">
      <polygon points="0,0 532,0 532,48 496,140 0,140" fill="var(--navy)"/>
      <polygon points="0,140 496,140 532,48 532,70 504,156 0,156" fill="var(--sky)"/>
    </svg>
    <div class="brand-lockup">
      <span class="brand-dot"></span>
      <span class="brand-name">PolarGust</span>
    </div>

    <h1 class="headline"><span class="size">18”</span> High Performance Oscillating</h1>
    <h2 class="product-type"><span class="word-pedestal">Pedestal</span><span class="word-fan">Fan</span></h2>

    <p class="feature-tilt">
      <span class="lead">Variable Positions</span>
      <span class="small">for Optimum comfort</span>
      <span class="lead">Tilting Head</span>
    </p>

    <svg class="tilt-icon" viewBox="0 0 130 120" role="img" aria-label="Tilting fan head with rotation arrows">
      <path d="M30 70 A40 40 0 0 1 55 18" fill="none" stroke="var(--navy)" stroke-width="8"/>
      <path d="M100 70 A40 40 0 0 0 75 18" fill="none" stroke="var(--navy)" stroke-width="8"/>
      <polygon points="20,66 40,66 30,82" fill="var(--navy)"/>
      <polygon points="90,66 110,66 100,82" fill="var(--navy)"/>
      <path d="M14 88 Q65 118 116 88" fill="none" stroke="var(--sky)" stroke-width="8"/>
      <polygon points="8,80 24,86 12,98" fill="var(--sky)"/>
      <polygon points="122,80 106,86 118,98" fill="var(--sky)"/>
      <ellipse cx="62" cy="50" rx="14" ry="22" fill="var(--fan-dark)"/>
      <rect x="63" y="60" width="3" height="30" fill="var(--fan-dark)"/>
    </svg>

    <p class="feature-positions">Selectable<br>Stationary<br>Positions</p>

    <div class="product-photo" role="img" aria-label="Photo of the black 18 inch pedestal fan on its round base"></div>

    <p class="feature-height">Adjustable<br>Height from<br>41”to 52”</p>

    <p class="model-name">GaleSpin</p>
  </main>
</body>
</html>
```